Stationery/business card design for "Mobile Echoscan Partners LLC"
Mobile Echoscan Partners, LLC
Professional
Tariq Velmont, RDMS
Director of Operations
27836 Brevard Lane,
Harlow Springs, Nevada, 70318
info@mobileechoscanpartners.example
www.mobileechoscanpartners.example
There will be two names on the business cards. The names and titles are the following;
Farida Kostral
Sales and Marketing
This is the logo design

```html
<!DOCTYPE html>
<html lang="en">
<head>
<meta charset="utf-8">
<title>Mobile Echoscan Partners, LLC – Business Card</title>
<link rel="stylesheet" href="https://fonts.googleapis.com/css2?family=Cinzel:wght@500&family=Crimson+Text:wght@400;600&display=swap">
<style>
  :root {
    --bg: #e9eaec;
    --blue: #1f6fa6;
    --blue-deep: #184f86;
    --blue-light: #2e86c1;
    --grey: #8d8f93;
    --ink: #3c3f44;
    --card-white: #f7f7f7;
    --white: #ffffff;
  }
  * { margin: 0; padding: 0; box-sizing: border-box; }
  html, body { width: 1200px; height: 931px; overflow: hidden; background: var(--bg); }
  .canvas { position: relative; width: 1200px; height: 931px; }
  .card {
    position: absolute; width: 560px; height: 320px; border-radius: 14px; overflow: hidden;
    box-shadow: 0 10px 28px rgba(0,0,0,.18);
  }
  .card-front { left: 60px; top: 130px; background: linear-gradient(160deg, var(--white), var(--card-white) 60%, #e6e6e6); }
  .card-back { left: 580px; top: 480px; background: linear-gradient(135deg, var(--blue-light), var(--blue-deep)); }
  .card-art { position: absolute; inset: 0; }
  .brand { position: absolute; text-align: center; font-family: 'Cinzel', serif; font-weight: 500; }
  .brand-name { font-size: 21px; line-height: 1.15; letter-spacing: .5px; }
  .brand-mark { display: inline-block; width: 34px; height: 34px; border-radius: 50%; margin-bottom: 8px; }
  .brand-tagline { font-family: 'Crimson Text', serif; font-size: 10px; letter-spacing: 1.4px; text-transform: uppercase; margin-top: 4px; padding-top: 3px; white-space: nowrap; }
  .card-front .brand { left: 210px; top: 72px; width: 230px; color: var(--blue-deep); }
  .card-front .brand-mark { background: var(--blue); }
  .card-front .brand-tagline { color: var(--ink); border-top: 1px solid var(--grey); }
  .card-back .brand { left: 260px; top: 150px; width: 260px; color: var(--white); }
  .card-back .brand-mark { background: var(--white); }
  .card-back .brand-tagline { border-top: 1px solid rgba(255,255,255,.7); }
  .contacts { position: absolute; left: 28px; top: 150px; font-family: 'Crimson Text', serif; color: var(--ink); font-size: 11px; line-height: 1.35; }
  .person-name { font-size: 14px; color: var(--blue); font-weight: 600; }
  .person-title { color: var(--ink); }
  .person { margin-bottom: 10px; }
  .line { display: flex; align-items: center; gap: 5px; }
  .line svg { width: 9px; height: 9px; flex: none; }
  .row { display: flex; gap: 26px; }
</style>
</head>
<body>
<main class="canvas">
  <section class="card card-front" aria-label="Business card front">
    <svg class="card-art" viewBox="0 0 560 320" aria-hidden="true">
      <path d="M380 0 H560 V320 H545 C520 190 470 80 380 0 Z" fill="#1f6fa6"/>
      <path d="M350 0 H382 C470 80 520 190 545 320 H528 C500 190 440 80 350 0 Z" fill="#8d8f93"/>
      <path d="M340 0 H352 C440 80 500 190 528 320 H520 C490 190 430 80 340 0 Z" fill="#ffffff"/>
    </svg>
    <div class="brand">
      <span class="brand-mark"></span>
      <div class="brand-name">Mobile Echoscan<br>Partners, LLC</div>
      <div class="brand-tagline">Clear scans, right at your door</div>
    </div>
    <div class="contacts">
      <div class="person">
        <div class="person-name">Tariq Velmont, RDMS</div>
        <div class="person-title">Director of Operations</div>
        <div class="line"><svg viewBox="0 0 10 10"><rect x="2.5" y="0.5" width="5" height="9" rx="1" fill="#1f6fa6"/></svg>713 555 0142</div>
      </div>
      <div class="row">
        <div class="person">
          <div class="person-name">Farida Kostral</div>
          <div class="person-title">Sales and Marketing</div>
        </div>
        <div>
          <div class="line"><svg viewBox="0 0 10 10"><rect x="2.5" y="0.5" width="5" height="9" rx="1" fill="#1f6fa6"/></svg>832 555 0187</div>
          <div class="line"><svg viewBox="0 0 10 10"><rect x="1" y="2" width="8" height="6" fill="#1f6fa6"/></svg>832 555 0163</div>
        </div>
      </div>
      <div>27836 Brevard Lane,</div>
      <div>Harlow Springs, Nevada, 70318</div>
      <div class="line" style="margin-top:6px"><svg viewBox="0 0 10 10"><rect x="0.5" y="2" width="9" height="6" fill="#1f6fa6"/></svg>info@mobileechoscanpartners.example</div>
      <div class="line"><svg viewBox="0 0 10 10"><circle cx="5" cy="5" r="4.5" fill="#1f6fa6"/></svg>www.mobileechoscanpartners.example</div>
    </div>
  </section>

  <section class="card card-back" aria-label="Business card back">
    <div class="brand">
      <span class="brand-mark"></span>
      <div class="brand-name">Mobile Echoscan<br>Partners, LLC</div>
      <div class="brand-tagline">Clear scans, right at your door</div>
    </div>
  </section>
</main>
</body>
</html>
```